FOOD DELIVERY BRAND NEEDS WEBSITE TO GET SUBSCRIBERS

web design needed for a food delivery brand/label,
website should display who we are, how it works and push futur clients to get the label for an online application. Should look serious/official, trustworthy and confident. colors are black and gold like logo

Target Market(s)

restaurants

Industry/Entity Type

restaurant

Number of Pages Required

4 page

Requirements
Must have
• home page, who we are, our partners, subscribe, 2 subscribe button : 1 on top 1 bottom
Nice to have
• a graphic showing average + 15% sales thanks the label

```html
<!DOCTYPE html>
<html lang="en">
<head>
<meta charset="utf-8">
<title>Gildmark — Upload Images</title>
<link rel="stylesheet" href="https://fonts.googleapis.com/css2?family=Figtree:wght@400;500;600;700&display=swap">
<style>
  :root {
    --ink: #0d0d0d;
    --gold: #e0c37a;
    --gold-line: #8a7a50;
    --nav-text: #e8dfc6;
    --panel: #e3d9bb;
    --panel-text: #4a3f25;
    --box-border: #a89a74;
    --icon: #a6956b;
    --white: #ffffff;
  }
  * { box-sizing: border-box; margin: 0; padding: 0; }
  html, body {
    width: 1200px;
    height: 1000px;
    overflow: hidden;
    background: var(--ink);
    font-family: "Figtree", sans-serif;
  }
  .site-header {
    position: absolute;
    left: 0; top: 0;
    width: 1200px; height: 86px;
    border-bottom: 1px solid var(--gold-line);
  }
  .brand {
    position: absolute;
    left: 108px; top: 28px;
    display: flex; align-items: center; gap: 8px;
    color: var(--gold);
    font-size: 20px; font-weight: 700;
    text-decoration: none;
  }
  .brand-dot {
    width: 14px; height: 14px; border-radius: 50%;
    background: var(--gold);
  }
  .main-nav a {
    position: absolute;
    top: 32px;
    color: var(--nav-text);
    font-size: 15px;
    letter-spacing: 0.8px;
    text-decoration: none;
  }
  .nav-home { left: 618px; }
  .nav-who { left: 705px; }
  .nav-partners { left: 840px; }
  .btn-subscribe {
    position: absolute;
    left: 976px; top: 22px;
    width: 116px; height: 40px;
    border-radius: 20px;
    background: var(--gold);
    color: var(--ink);
    font-size: 15px; font-weight: 700;
    display: flex; align-items: center; justify-content: center;
    text-decoration: none;
  }
  .upload-panel {
    position: absolute;
    left: 209px; top: 132px;
    width: 782px; height: 449px;
    background: var(--panel);
    color: var(--panel-text);
    text-align: center;
  }
  .upload-title {
    position: absolute; left: 0; right: 0; top: 44px;
    font-size: 30px; font-weight: 700;
    letter-spacing: -0.3px;
  }
  .upload-hint {
    position: absolute; left: 0; right: 0; top: 90px;
    font-size: 18px; font-weight: 400;
  }
  .drop-zone {
    position: absolute; top: 158px;
    width: 192px; height: 128px;
    background: var(--white);
    border: 2px dashed var(--box-border);
  }
  .drop-zone-a { left: 179px; }
  .drop-zone-b { left: 397px; }
  .drop-icon {
    position: absolute; left: 63px; top: 18px;
    width: 62px; height: 62px;
  }
  .drop-label {
    position: absolute; left: 0; right: 0; top: 94px;
    font-size: 14px; color: #2f2a1c;
  }
  .drop-label u { text-underline-offset: 2px; }
  .btn-submit {
    position: absolute;
    left: 299px; top: 332px;
    width: 184px; height: 59px;
    border-radius: 30px;
    background: var(--ink);
    color: var(--gold);
    font-family: inherit;
    font-size: 19px; font-weight: 700;
    border: none;
  }
</style>
</head>
<body>
  <header class="site-header">
    <a class="brand" href="#"><span class="brand-dot"></span>Gildmark</a>
    <nav class="main-nav">
      <a class="nav-home" href="#">Home</a>
      <a class="nav-who" href="#">Who We Are</a>
      <a class="nav-partners" href="#">Our Partners</a>
    </nav>
    <a class="btn-subscribe" href="#">Subscribe</a>
  </header>

  <section class="upload-panel">
    <h1 class="upload-title">Images (up to 2)</h1>
    <p class="upload-hint">Upload photos not exceeding 3mb (JPG, PNG)</p>

    <div class="drop-zone drop-zone-a">
      <svg class="drop-icon" viewBox="0 0 62 62" fill="none" stroke="#a6956b" stroke-width="2.5">
        <rect x="1.5" y="1.5" width="59" height="59"/>
        <line x1="1.5" y1="50" x2="60.5" y2="50"/>
        <polyline points="6,43 24,26 36,40 44,33 54,43 6,43"/>
        <circle cx="36" cy="19" r="5"/>
      </svg>
      <p class="drop-label">Drag and drop or <u>upload</u></p>
    </div>

    <div class="drop-zone drop-zone-b">
      <svg class="drop-icon" viewBox="0 0 62 62" fill="none" stroke="#a6956b" stroke-width="2.5">
        <rect x="1.5" y="1.5" width="59" height="59"/>
        <line x1="1.5" y1="50" x2="60.5" y2="50"/>
        <polyline points="6,43 24,26 36,40 44,33 54,43 6,43"/>
        <circle cx="36" cy="19" r="5"/>
      </svg>
      <p class="drop-label">Drag and drop or <u>upload</u></p>
    </div>

    <button class="btn-submit" type="button">Submit</button>
  </section>
</body>
</html>
```